Product Image Design: Claiming the Salary You Deserve at Last (Plus Bonus!)

I need a product image designed for a new product I will be selling on sellvantrix.com that teaches how to quickly make more money by getting a raise or promotion.

Dimensions must be 1280 x 720 pixels. The product title and subtitle are as follows:

Title: Claiming the Full Salary You Deserve at Last (Plus Bonus!)

Subtitle: The Quickest Route toward a Huge Pay Bump Minus Costly Schooling Plus Flattering of Management

I'm looking for a design that is eye catching and communicates the idea of business success and getting paid more money from a company or employer.

The target audience is professional men in their 20s and 30s who are looking to quickly make more money and advance in their careers.

Target Market(s)

Professional men in their 20s and 30s who are looking to quickly make more money and advance in their careers.

Industry/Entity Type

Professional Service

Font styles to use
Serif

Requirements
Must have
• Title and subtitle provided in project description.

Final design in 1280 x 720 dimensions (or larger with same width to height ratio).

Eye catching font, colors and graphics, but not overly flashy.

Masculine colors (i.e. no pinks or other feminine colors).
Nice to have
• N/A
Should not have
• Feminine colors or images of women.

```html
<!DOCTYPE html>
<html lang="en">
<head>
<meta charset="utf-8">
<title>Claiming the Full Salary You Deserve at Last (Plus Bonus!)</title>
<link href="https://fonts.googleapis.com/css2?family=Cinzel:wght@400;500&family=Quicksand:wght@400&display=swap" rel="stylesheet">
<style>
  :root {
    --teal: #009db3;
    --ink: #0d0d0d;
    --paper: #ffffff;
    --mist: #e4e4e4;
    --stage: #4d4d4d;
    --orb: #e6e6e6;
    --dot: #b9b9b9;
    --tile: #b7dde3;
    --gold: #e8b42e;
    --steel: #cfcfcf;
  }
  html, body {
    margin: 0;
    padding: 0;
    width: 1200px;
    height: 773px;
    overflow: hidden;
    background: var(--stage);
  }
  .product-card {
    position: absolute;
    left: 0;
    top: 49px;
    width: 1200px;
    height: 675px;
    overflow: hidden;
    background: linear-gradient(to bottom, var(--paper) 30%, var(--mist) 85%);
  }
  .backdrop {
    position: absolute;
    inset: 0;
    width: 1200px;
    height: 675px;
  }
  .dot-grid {
    position: absolute;
    left: 196px; top: 75px; width: 37px; height: 38px;
    background: var(--dot); opacity: .55; border-radius: 3px;
  }
  .tile-grid {
    position: absolute;
    left: 688px; top: 45px; width: 56px; height: 56px;
    background: var(--tile); border-radius: 2px;
  }
  .hero-illustration {
    position: absolute;
    left: 745px; top: 115px; width: 400px; height: 470px;
    background: linear-gradient(200deg, var(--steel) 0%, #e9c46a 55%, var(--gold) 100%);
    border-radius: 46% 46% 30% 30%;
    opacity: .85;
  }
  .title-block {
    margin: 0;
    font-family: "Cinzel", "Times New Roman", serif;
    font-weight: 400;
    color: var(--ink);
  }
  .title-line {
    position: absolute;
    left: 120px;
    line-height: 1;
    white-space: nowrap;
    letter-spacing: 1px;
  }
  .title-lead { top: 153px; font-size: 52px; }
  .title-accent {
    top: 196px; left: 116px;
    font-size: 100px;
    font-weight: 500;
    color: var(--teal);
  }
  .title-body { top: 289px; font-size: 50px; }
  .title-tail { top: 339px; font-size: 50px; }
  .subtitle {
    position: absolute;
    left: 106px;
    top: 398px;
    width: 590px;
    margin: 0;
    font-family: "Quicksand", "Helvetica", sans-serif;
    font-size: 19.5px;
    line-height: 26px;
    color: var(--teal);
  }
  .cta-button {
    position: absolute;
    left: 256px;
    top: 490px;
    width: 238px;
    height: 48px;
    border: 1.5px solid var(--teal);
    display: flex;
    align-items: center;
    justify-content: center;
    font-family: "Quicksand", "Helvetica", sans-serif;
    font-size: 18px;
    color: var(--teal);
    text-decoration: none;
    box-sizing: border-box;
  }
</style>
</head>
<body>
  <main class="product-card">
    <svg class="backdrop" viewBox="0 0 1200 675" aria-hidden="true">
      <path class="blob-top-left" fill="var(--teal)"
        d="M0 0 H432 C420 30 360 49 300 49 C240 49 200 45 180 70 C150 110 130 140 60 165 C30 178 47 195 47 240 C47 275 20 292 0 299 Z"/>
      <path class="blob-top-right" fill="var(--teal)"
        d="M925 0 H1200 V136 C1185 115 1175 90 1155 82 C1130 72 1100 70 1060 70 C1000 70 925 50 925 13 Z"/>
      <circle class="floating-orb" cx="798" cy="212" r="30" fill="var(--orb)"/>
    </svg>

    <div class="dot-grid" role="img" aria-label="Small grey dot pattern accent"></div>
    <div class="tile-grid" role="img" aria-label="Small light teal square tile pattern accent"></div>

    <div class="hero-illustration" role="img"
      aria-label="Illustration of a businessman riding a rocket upward over a rising golden arrow"></div>

    <svg class="backdrop" viewBox="0 0 1200 675" aria-hidden="true">
      <path class="cloud-bank" fill="var(--paper)"
        d="M0 470 C25 450 80 448 122 476 C138 490 130 525 131 545 C160 552 172 575 168 598 C190 595 200 602 205 610 C240 600 290 602 330 614 C360 598 410 602 440 618 C470 598 500 603 516 614 C560 570 640 560 700 592 C760 545 880 560 980 620 C990 604 1020 600 1035 606 C1040 590 1055 572 1075 566 C1100 560 1110 570 1118 565 C1130 520 1160 505 1200 502 V675 H0 Z"/>
      <path class="cloud-right" fill="var(--paper)"
        d="M1048 557 C1052 490 1110 450 1200 452 V675 H1040 Z"/>
    </svg>

    <h1 class="title-block">
      <span class="title-line title-lead">Claiming the Full</span>
      <span class="title-line title-accent">Salary</span>
      <span class="title-line title-body">You Deserve at Last</span>
      <span class="title-line title-tail">(Plus Bonus!)</span>
    </h1>

    <p class="subtitle">The Quickest Route toward a Huge Pay Bump Minus Costly Schooling Plus Flattering of Management</p>

    <a class="cta-button" href="#">KNOW MORE</a>
  </main>
</body>
</html>
```